Business Card Design Project

Hello
I want a Simple Business card that uses the company logo that is easily reasonable but looks professional as I am an IT Services company and would look to share these cards with prospective clients.
The details are:
Kestrel Arc Solutions
14 Morrow Lane
Birmingham
B7 4QX
Telephone 0845 217 6640
I would like my name Oliver Hastings and my title Director on the card.
Target Market(s)
IT Professionals
Industry/Entity Type
Business

```html
<!DOCTYPE html>
<html lang="en">
<head>
<meta charset="utf-8">
<title>Kestrel Arc Solutions – Business Card</title>
<link href="https://fonts.googleapis.com/css2?family=Open+Sans:wght@300;400;700;800&display=swap" rel="stylesheet">
<style>
  :root {
    --stage: #e6e4e1;
    --card: #fdfdfd;
    --ink: #1e1c1d;
    --leaf: #5cb137;
    --rule: #3a3839;
    --paper-text: #2b2a2a;
  }
  * { box-sizing: border-box; margin: 0; padding: 0; }
  html, body {
    width: 1200px; height: 675px; overflow: hidden;
    background: var(--stage);
    font-family: "Open Sans", Arial, sans-serif;
  }
  .card {
    position: absolute; left: 160px; top: 86px;
    width: 880px; height: 503px;
    background: var(--card);
    box-shadow: 0 10px 30px rgba(0,0,0,.12);
  }
  .card-frame { position: absolute; inset: 0; }
  .brand {
    position: absolute; top: 62px; left: 0; right: 0;
    display: flex; justify-content: center; align-items: center; gap: 12px;
  }
  .brand-dot { width: 26px; height: 26px; border-radius: 50%; background: var(--leaf); }
  .brand-name { font-size: 32px; font-weight: 700; color: var(--ink); letter-spacing: -0.5px; }
  .holder-name {
    position: absolute; top: 138px; left: 0; right: 0; text-align: center;
    font-size: 50px; font-weight: 800; color: var(--leaf); letter-spacing: -0.5px;
  }
  .holder-title {
    position: absolute; top: 206px; left: 470px;
    font-size: 15px; font-weight: 700; color: var(--ink);
  }
  .phone-band { position: absolute; top: 232px; left: 120px; width: 640px; height: 66px; }
  .phone-number {
    position: absolute; top: 232px; left: 120px; width: 640px; height: 66px;
    display: flex; align-items: center; justify-content: center;
    font-size: 38px; font-weight: 300; color: #fff; letter-spacing: 2px;
  }
  .address {
    position: absolute; top: 318px; left: 200px; width: 480px;
    display: flex; justify-content: space-between;
    font-size: 13px; color: var(--paper-text); text-transform: uppercase; letter-spacing: .5px;
  }
  .rule { position: absolute; left: 200px; width: 480px; height: 1px; background: var(--rule); }
  .rule-top { top: 350px; }
  .rule-bottom { top: 398px; }
  .divider-ornament {
    position: absolute; top: 344px; left: 420px; width: 40px; height: 12px;
    background: var(--card); border: 1px solid var(--rule);
  }
  .company-line {
    position: absolute; top: 364px; left: 0; right: 0; text-align: center;
    font-size: 14px; color: var(--paper-text);
  }
</style>
</head>
<body>
  <div class="card">
    <svg class="card-frame" width="880" height="503" viewBox="0 0 880 503" aria-hidden="true">
      <rect x="26" y="26" width="828" height="451" fill="none" stroke="#3a3839" stroke-width="1.5"/>
      <rect x="33" y="33" width="814" height="437" fill="none" stroke="#3a3839" stroke-width="1"/>
      <rect x="20" y="20" width="16" height="16" fill="#2a2829"/>
      <rect x="844" y="20" width="16" height="16" fill="#2a2829"/>
      <rect x="20" y="467" width="16" height="16" fill="#2a2829"/>
      <rect x="844" y="467" width="16" height="16" fill="#2a2829"/>
    </svg>

    <div class="brand">
      <span class="brand-dot"></span>
      <span class="brand-name">Kestrel Arc Solutions</span>
    </div>

    <h1 class="holder-name">Oliver Hastings</h1>
    <p class="holder-title">Director</p>

    <svg class="phone-band" width="640" height="66" viewBox="0 0 640 66" aria-hidden="true">
      <polygon points="14,0 626,0 626,10 640,10 640,56 626,56 626,66 14,66 14,56 0,56 0,10 14,10" fill="#1e1c1d"/>
    </svg>
    <p class="phone-number">0845 217 6640</p>

    <div class="address">
      <span>14 Morrow Lane</span>
      <span>Birmingham</span>
      <span>B7 4QX</span>
    </div>

    <div class="rule rule-top"></div>
    <div class="divider-ornament" role="img" aria-label="Small decorative divider"></div>
    <p class="company-line">Kestrel Arc Solutions</p>
    <div class="rule rule-bottom"></div>
  </div>
</body>
</html>
```